Branding label contest for 2 great products

I require labels for our health food treat dry packs and coffee business. The packaging at this stage consists of the follow... plastic food pouches for dry ingredients and takeaway coffee cups. The coffee cup artwork/design will be for standard small, medium and large paper takeaway coffee cups and the food pouch size 190mmW x 260mmL. the pouch design will need to be customisable to allow use across a range of products. for reference please visit www.torvimunda.com.au and instagram @torvimunda for products. I have attached our logo and business card files for your perusal.

Target Market(s)

Healthy conscious, vegan, paleo, gluten free, all round fitness fanatics and yogis

Industry/Entity Type

Business

Requirements
Must have
• Earthy tones, our logo. Rustic earthy feel. trendy artwork.
Should not have
• Bright colours

```html
<!DOCTYPE html>
<html lang="en">
<head>
<meta charset="utf-8">
<title>Torvi Munda – Cacao Nibs Pouch</title>
<link href="https://fonts.googleapis.com/css2?family=Bebas+Neue&family=Amatic+SC:wght@700&family=Arvo&family=Josefin+Sans:wght@400&display=swap" rel="stylesheet">
<style>
  :root {
    --bg: #ffffff;
    --film: #f3f3f3;
    --film-edge: #e2e2e2;
    --nib-dark: #3b2622;
    --nib-mid: #6a4338;
    --nib-light: #8a5e4c;
    --kraft: #c59b63;
    --kraft-light: #cfa874;
    --ink: #4a2a1f;
    --badge: #ffffff;
    --badge-ink: #a69a86;
  }
  html, body {
    margin: 0;
    padding: 0;
    width: 1200px;
    height: 1200px;
    overflow: hidden;
    background: var(--bg);
  }
  .canvas {
    position: relative;
    width: 1200px;
    height: 1200px;
  }
  .pouch {
    position: absolute;
    left: 258px;
    top: 86px;
    width: 686px;
    height: 1058px;
    border-radius: 6px 6px 4px 4px;
    overflow: hidden;
  }
  .pouch-seal {
    position: absolute;
    left: 0; top: 0;
    width: 100%;
    height: 204px;
    background: linear-gradient(180deg, var(--film) 0%, #fafafa 40%, var(--film) 100%);
    border-bottom: 1px solid var(--film-edge);
  }
  .pouch-seal::after {
    content: "";
    position: absolute;
    left: 0; right: 0;
    top: 120px;
    height: 6px;
    background: var(--film-edge);
    opacity: .6;
  }
  .pouch-contents {
    position: absolute;
    left: 0; top: 204px;
    width: 100%;
    height: 854px;
    background:
      radial-gradient(circle at 20% 30%, var(--nib-light) 0%, transparent 35%),
      radial-gradient(circle at 80% 70%, var(--nib-light) 0%, transparent 35%),
      linear-gradient(160deg, var(--nib-mid) 0%, var(--nib-dark) 55%, var(--nib-mid) 100%);
  }
  .label {
    position: absolute;
    left: 432px;
    top: 352px;
    width: 338px;
    height: 762px;
    background: linear-gradient(170deg, var(--kraft-light) 0%, var(--kraft) 60%, #bf945b 100%);
    color: var(--ink);
    text-align: center;
  }
  .brand-badge {
    position: absolute;
    left: 506px;
    top: 258px;
    width: 188px;
    height: 188px;
    border-radius: 50%;
    background: var(--badge);
    display: flex;
    align-items: center;
    justify-content: center;
    box-shadow: 0 0 0 1px rgba(0,0,0,.03);
  }
  .brand-name {
    font-family: "Josefin Sans", sans-serif;
    font-weight: 400;
    font-size: 22px;
    letter-spacing: 3px;
    color: var(--badge-ink);
    text-transform: uppercase;
    line-height: 1.3;
    text-align: center;
  }
  .product-title {
    position: absolute;
    left: 0; right: 0;
    top: 132px;
    margin: 0;
    font-family: "Bebas Neue", sans-serif;
    font-weight: 400;
    font-size: 152px;
    line-height: 136px;
    letter-spacing: 1px;
  }
  .tagline {
    position: absolute;
    left: 0; right: 0;
    top: 418px;
    font-family: "Amatic SC", sans-serif;
    font-weight: 700;
    font-size: 50px;
    letter-spacing: 4px;
    line-height: 1;
  }
  .flower-art {
    position: absolute;
    left: 124px;
    top: 486px;
    width: 96px;
    height: 96px;
    border-radius: 50%;
    background: radial-gradient(circle, rgba(74,42,31,.35) 0%, rgba(74,42,31,.08) 65%, transparent 70%);
  }
  .divider {
    position: absolute;
    left: 32px;
    right: 30px;
    border-top: 2px dashed var(--ink);
  }
  .divider.top { top: 614px; }
  .divider.bottom { top: 728px; }
  .diet-list {
    position: absolute;
    left: 0; right: 0;
    top: 634px;
    font-family: "Arvo", serif;
    font-size: 22px;
    line-height: 28px;
  }
</style>
</head>
<body>
<div class="canvas">
  <div class="pouch">
    <div class="pouch-seal"></div>
    <div class="pouch-contents" role="img" aria-label="Photograph of cacao nibs filling the pouch"></div>
  </div>

  <div class="label">
    <h1 class="product-title">CACAO<br>NIBS</h1>
    <div class="tagline">BETTER FOR YOU</div>
    <div class="flower-art" role="img" aria-label="Hand-drawn star anise flower illustration"></div>
    <div class="divider top"></div>
    <p class="diet-list" style="margin:0">vegan, gluten-free,<br>paleo, dairy-free,<br>grain-free</p>
    <div class="divider bottom"></div>
  </div>

  <div class="brand-badge">
    <span class="brand-name">Torvi<br>Munda</span>
  </div>
</div>
</body>
</html>
```